Fun relaxed Travel Photography Business Card*

Require a fun, funky and quirky but rememberable business card for a travel photographer

Industry/Entity Type

Photographer

Contact Information for Business Card

Front Card

(my name) Tavo M.

Travel Photographer ( small under travel photographer) “self-proclaimed”

(website logo) wanderingtavo.example

(Snapfeed logo) @wandering_with_tavo

(Snapfeed logo) @wandering_with_tavo_2.0 (backup for when Snapfeed puts Tavo on timeout for bad behaviour)

Tel: N/A (removing the potential awkwardness of me not replying)

Email: (see above)

Back Card

Offending people since 1986

(Bottom right corner) “p.s. travelling made me fatTER”

Font styles to use
Serif

Colors

Designer to choose colors to be used in the design.

Requirements
Must have
• a camera
• a similar cartoon version of me as the "logo" see attached files, try to make as similar as possible

```html
<!DOCTYPE html>
<html lang="en">
<head>
<meta charset="utf-8">
<title>Tavo M. – Travel Photographer Business Card</title>
<link rel="stylesheet" href="https://fonts.googleapis.com/css2?family=Kaushan+Script&family=Yanone+Kaffeesatz:wght@400;500&family=Caveat:wght@500;600&display=swap">
<style>
  :root {
    --stage: #d6d6d6;
    --card-red: #c8102e;
    --deep-red: #9e0f25;
    --paper: #ffffff;
    --ink: #1a1a1a;
    --sky: #4aa8e0;
    --sky-light: #8fd0f2;
    --camera-grey: #cfcfcf;
    --plane-grey: #e6e6e6;
  }
  * { box-sizing: border-box; margin: 0; padding: 0; }
  html, body { width: 1200px; height: 1200px; overflow: hidden; }
  body { background: var(--stage); position: relative; }

  .card {
    position: absolute;
    top: 231px;
    width: 422px;
    height: 738px;
    overflow: hidden;
  }
  .card--front { left: 66px; background: var(--card-red); color: var(--paper); }
  .card--back { left: 667px; background: var(--paper); }
  .card-shape { position: absolute; inset: 0; width: 422px; height: 738px; }
  .abs { position: absolute; }

  .name {
    top: 30px; left: 0; width: 100%; text-align: center;
    font-family: "Kaushan Script", cursive; font-weight: 400;
    font-size: 66px; line-height: 1;
  }
  .title {
    top: 136px; left: 0; width: 100%; text-align: center;
    font-family: "Yanone Kaffeesatz", sans-serif; font-weight: 500;
    font-size: 29px; letter-spacing: 1.5px; line-height: 1;
  }
  .title-note {
    top: 162px; left: 126px;
    font-family: "Caveat", cursive; font-weight: 600;
    font-size: 30px; color: var(--ink); line-height: 1;
  }

  .contact-list { top: 262px; left: 70px; list-style: none; }
  .contact-item {
    display: flex; align-items: center; gap: 8px; height: 35px;
    font-family: "Caveat", cursive; font-weight: 600; font-size: 25px;
  }
  .contact-icon { width: 24px; height: 24px; flex: none; }
  .network-name { font-size: 20px; }
  .contact-remark {
    top: 368px; left: 108px;
    font-family: "Yanone Kaffeesatz", sans-serif; font-size: 20px; line-height: 26px;
  }

  .phone-row { top: 478px; left: 40px; display: flex; gap: 10px; }
  .phone-label {
    font-family: "Yanone Kaffeesatz", sans-serif; font-size: 25px; line-height: 30px;
  }
  .phone-remark {
    top: 508px; left: 66px;
    font-family: "Yanone Kaffeesatz", sans-serif; font-size: 18px; line-height: 20px;
  }
  .email-row {
    top: 572px; left: 38px; display: flex; align-items: center; gap: 10px;
    font-family: "Yanone Kaffeesatz", sans-serif; font-size: 22px; line-height: 30px;
  }

  .plane-art {
    top: 468px; left: 222px; width: 150px; height: 160px; border-radius: 50%;
    background: linear-gradient(135deg, #f7f7f7 0%, var(--plane-grey) 100%);
  }

  .portrait {
    top: 36px; left: 62px; width: 294px; height: 294px; border-radius: 50%;
    border: 6px solid var(--card-red);
    background: linear-gradient(170deg, var(--sky-light) 0%, var(--sky) 60%, #3b8fc4 100%);
  }
  .camera-art {
    top: 345px; left: 163px; width: 96px; height: 78px; border-radius: 10px;
    background: linear-gradient(180deg, #eeeeee 0%, var(--camera-grey) 100%);
  }
  .tagline {
    top: 430px; left: 0; width: 100%; text-align: center;
    font-family: "Caveat", cursive; font-weight: 600;
    color: var(--deep-red); line-height: 44px;
  }
  .tagline-main { font-size: 44px; display: block; padding-left: 10px; }
  .tagline-sub { font-size: 38px; display: block; padding-left: 10px; }
  .postscript {
    top: 598px; left: 36px;
    font-family: "Yanone Kaffeesatz", sans-serif; font-size: 34px;
    line-height: 40px; color: var(--paper);
  }
  .postscript-line2 { display: block; padding-left: 13px; }
</style>
</head>
<body>

<section class="card card--front" aria-label="Business card front">
  <svg class="card-shape" viewBox="0 0 422 738" aria-hidden="true">
    <path fill="var(--paper)" d="M0,588 C50,650 170,680 235,632 L250,642 C262,700 300,702 330,706 C360,690 400,690 422,672 L422,738 L0,738 Z"/>
    <g fill="var(--paper)">
      <circle cx="213" cy="627" r="11"/>
      <circle cx="269" cy="607" r="8"/>
      <circle cx="294" cy="656" r="17"/>
      <circle cx="385" cy="664" r="8"/>
    </g>
  </svg>

  <h1 class="abs name">Tavo M.</h1>
  <p class="abs title">TRAVEL PHOTOGRAPHER</p>
  <p class="abs title-note">self-proclaimed</p>

  <ul class="abs contact-list">
    <li class="contact-item">
      <svg class="contact-icon" viewBox="0 0 24 24" aria-hidden="true">
        <circle cx="12" cy="12" r="11" fill="#2d6fc0" stroke="#fff" stroke-width="1.5"/>
        <ellipse cx="12" cy="12" rx="5" ry="10" fill="none" stroke="#fff" stroke-width="1.3"/>
        <line x1="2" y1="12" x2="22" y2="12" stroke="#fff" stroke-width="1.3"/>
      </svg>
      <span>wanderingtavo.example</span>
    </li>
    <li class="contact-item"><span class="network-name">Snapfeed</span><span>@wandering_with_tavo</span></li>
    <li class="contact-item"><span class="network-name">Snapfeed</span><span>@wandering_with_tavo_2.0</span></li>
  </ul>
  <p class="abs contact-remark">(backup for when Snapfeed puts<br>Tavo on timeout for bad behaviour)</p>

  <div class="abs plane-art" role="img" aria-label="Illustration of a white airliner flying upward to the right"></div>

  <div class="abs phone-row">
    <svg width="16" height="26" viewBox="0 0 16 26" aria-hidden="true">
      <rect x="1.5" y="1.5" width="13" height="23" rx="2" fill="none" stroke="#fff" stroke-width="2"/>
      <line x1="6" y1="21" x2="10" y2="21" stroke="#fff" stroke-width="1.5"/>
    </svg>
    <span class="phone-label">N/A</span>
  </div>
  <p class="abs phone-remark">(removing the potential<br>awkwardness of me<br>not replying)</p>
  <div class="abs email-row">
    <svg width="20" height="14" viewBox="0 0 20 14" aria-hidden="true">
      <rect x="0" y="0" width="20" height="14" fill="#fff"/>
      <path d="M0,0 L10,8 L20,0" fill="none" stroke="var(--card-red)" stroke-width="1.5"/>
    </svg>
    <span>(see above)</span>
  </div>
</section>

<section class="card card--back" aria-label="Business card back">
  <svg class="card-shape" viewBox="0 0 422 738" aria-hidden="true">
    <path fill="var(--card-red)" d="M0,560 C30,540 60,520 90,535 C110,518 150,520 165,550 C190,572 212,545 240,570 C270,592 300,540 340,545 C380,530 410,558 422,570 L422,738 L0,738 Z"/>
    <g fill="var(--paper)">
      <circle cx="37" cy="537" r="7"/>
      <circle cx="200" cy="574" r="11"/>
      <circle cx="332" cy="605" r="25"/>
      <circle cx="304" cy="669" r="15"/>
      <circle cx="352" cy="661" r="7"/>
    </g>
  </svg>

  <div class="abs portrait" role="img" aria-label="Cartoon avatar of the photographer in sunglasses and a floral shirt against a blue sky"></div>
  <div class="abs camera-art" role="img" aria-label="Illustration of a camera hanging on a strap"></div>

  <p class="abs tagline">
    <span class="tagline-main">Offending people</span>
    <span class="tagline-sub">since 1986</span>
  </p>

  <p class="abs postscript">PS. traveling<span class="postscript-line2">made me fatTER</span></p>
</section>

</body>
</html>
```